Business card design needed

Our modern electrical contracting company requires business card design utilising our logo and incorporating our tag line "Service when you need it". We specialise in assisting our customers 24/7 offering a breakdown service.

Industry/Entity Type

Electrical

Contact Information for Business Card

Marcus Penhale, Electrical contractor,Tel: (08) 8456 3071, Fax: (08) 8679 4315, Mob 0438 562 740, Email: marcus.penhale@brightwirepower.com.au, Web: www.brightwirepower.com.au

Requirements
Must have
• we require a 2 sided card.
Front- Logo, tag line and contact information.
Rear- service when you need it! Call now for our 24/7 breakdown service

```html
<!DOCTYPE html>
<html lang="en">
<head>
<meta charset="utf-8">
<title>Brightwire Power – Business Card</title>
<link rel="stylesheet" href="https://fonts.googleapis.com/css2?family=Source+Sans+3:wght@400;700&family=Tinos&display=swap">
<style>
  :root {
    --stage: #e4e5e7;
    --sky: #5c9cd6;
    --slate: #575757;
    --band: #e6e6e1;
    --brand: #2a52a8;
    --white: #ffffff;
    --soft-white: rgba(255, 255, 255, 0.78);
    --phone-blue: #5e9fd8;
  }
  * { margin: 0; padding: 0; box-sizing: border-box; }
  html, body {
    width: 1200px; height: 1067px; overflow: hidden;
    background: var(--stage);
    font-family: "Source Sans 3", "Myriad Pro", sans-serif;
  }
  .card {
    position: absolute; left: 215px; width: 725px; height: 415px; overflow: hidden;
  }
  .card--front { top: 73px; }
  .card--back { top: 548px; }
  .card__bg { position: absolute; inset: 0; width: 100%; height: 100%; }
  .card__text { position: absolute; white-space: nowrap; }

  .contact-web { left: 31px; top: 44px; font-size: 17px; color: var(--white); line-height: 22px; }
  .contact-web span { display: block; }
  .contact-web span + span { padding-left: 33px; }

  .person { right: 37px; top: 50px; text-align: right; color: var(--white); font-size: 21px; line-height: 28px; }
  .person__role { display: block; }

  .phones { left: 492px; top: 122px; color: var(--white); font-size: 16px; line-height: 21px; }
  .phones span { display: block; }

  .brand-mark {
    position: absolute; left: 286px; top: 105px; width: 164px; height: 164px;
    border-radius: 50%; background: var(--brand);
  }
  .brand-name {
    left: 0; right: 0; top: 298px; text-align: center;
    font-size: 53px; font-weight: 700; color: var(--brand); letter-spacing: 0.5px;
  }
  .brand-tagline {
    left: 0; right: 0; top: 360px; text-align: center;
    font-family: "Tinos", "Times New Roman", serif; font-size: 20px; color: var(--brand);
  }

  .back-tagline { left: 16px; top: 106px; font-size: 30px; color: var(--soft-white); }
  .back-call { left: 375px; top: 271px; font-size: 17px; color: var(--white); }
  .back-phone { left: 375px; top: 294px; font-size: 28px; color: var(--phone-blue); letter-spacing: 0.5px; }
</style>
</head>
<body>

<section class="card card--front" aria-label="Card front">
  <svg class="card__bg" viewBox="0 0 725 415" preserveAspectRatio="none" aria-hidden="true">
    <rect width="725" height="415" fill="var(--sky)"/>
    <polygon points="512,0 725,0 725,267 319,267" fill="var(--slate)"/>
    <rect y="267" width="725" height="148" fill="var(--band)"/>
  </svg>

  <p class="card__text contact-web">
    <span>Email: marcus.penhale@brightwirepower.com.au</span>
    <span>www.brightwirepower.com.au</span>
  </p>

  <p class="card__text person">
    <span class="person__name">Marcus Penhale</span>
    <span class="person__role">Electrical contractor</span>
  </p>

  <p class="card__text phones">
    <span>Tel: (08) 8456 3071,</span>
    <span>Fax: (08) 8679 4315,</span>
    <span>Mob 0438 562 740,</span>
  </p>

  <div class="brand-mark" aria-hidden="true"></div>
  <p class="card__text brand-name">BRIGHTWIRE POWER</p>
  <p class="card__text brand-tagline">Service when you need it</p>
</section>

<section class="card card--back" aria-label="Card back">
  <svg class="card__bg" viewBox="0 0 725 415" preserveAspectRatio="none" aria-hidden="true">
    <rect width="725" height="415" fill="var(--sky)"/>
    <polygon points="516,0 725,0 725,415 361,415 361,168" fill="var(--slate)"/>
  </svg>

  <p class="card__text back-tagline">Service when you need it!</p>
  <p class="card__text back-call">Call now for our 24/7 breakdown service</p>
  <p class="card__text back-phone">(08) 8456 3071</p>
</section>

</body>
</html>
```